Mindfulness School for Children -- Business Cards

We're looking for business cards for our school directors and owners. We're a mindfulness school for children called tumbling willows. Attached are our logos/icons.

```html
<!DOCTYPE html>
<html lang="en">
<head>
<meta charset="utf-8">
<title>Tumbling Willows – Business Card</title>
<link href="https://fonts.googleapis.com/css2?family=Inter:wght@400;500;600&family=Zilla+Slab:wght@500;700&display=swap" rel="stylesheet">
<style>
  :root {
    --canvas-bg: #c2e6ed;
    --card-white: #ffffff;
    --band-pale: #e3f3f4;
    --wash-blue: #7fb2c2;
    --wash-teal: #8cc3c6;
    --wash-green: #9fd0b0;
    --brand-teal: #5aa9b4;
    --disc-teal: #6bb7b2;
    --label-ink: #111111;
    --on-wash: #ffffff;
  }
  * { margin: 0; padding: 0; box-sizing: border-box; }
  html, body {
    width: 1200px; height: 1200px; overflow: hidden;
    background: var(--canvas-bg);
  }
  .canvas { position: relative; width: 1200px; height: 1200px; }
  .side-label {
    position: absolute; left: 236px;
    font-family: "Inter", sans-serif; font-size: 23px; font-weight: 400;
    color: var(--label-ink); letter-spacing: 0.3px;
  }
  .side-label--front { top: 99px; }
  .side-label--back { top: 626px; }
  .card {
    position: absolute; left: 238px; width: 724px; height: 414px;
    filter: drop-shadow(0 3px 6px rgba(40, 90, 100, 0.28));
  }
  .card--front { top: 141px; }
  .card--back { top: 665px; }
  .wordmark { font-family: "Zilla Slab", serif; font-weight: 500; }
  .person-name { font-family: "Zilla Slab", serif; font-weight: 700; }
  .person-role, .contact-text { font-family: "Inter", sans-serif; }
</style>
</head>
<body>
<main class="canvas">
  <p class="side-label side-label--front">FRONT</p>

  <svg class="card card--front" viewBox="0 0 1166 666" xmlns="http://www.w3.org/2000/svg">
    <defs>
      <linearGradient id="washTop" x1="0" y1="0" x2="1" y2="0">
        <stop offset="0" stop-color="#86bcc6"/>
        <stop offset="0.55" stop-color="#92c6c4"/>
        <stop offset="0.8" stop-color="#a2d3b1"/>
        <stop offset="1" stop-color="#94c9b9"/>
      </linearGradient>
      <linearGradient id="washBottom" x1="0" y1="0" x2="1" y2="1">
        <stop offset="0" stop-color="#7fb0c0"/>
        <stop offset="0.6" stop-color="#86b8c4"/>
        <stop offset="1" stop-color="#9ac8cc"/>
      </linearGradient>
    </defs>
    <rect class="card-base" width="1166" height="666" fill="var(--card-white)"/>
    <path class="wave-band" fill="var(--band-pale)" d="M58,0 C120,100 220,125 300,120 C420,110 480,42 580,42 C700,42 800,90 900,132 C1000,175 1080,238 1166,238 L1166,0 Z"/>
    <path class="wave-wash" role="img" aria-label="Soft blue-green watercolour wash" fill="url(#washTop)" d="M78,0 C140,78 230,92 300,90 C420,84 470,30 570,30 C690,30 800,78 920,122 C1020,160 1090,196 1166,196 L1166,0 Z"/>
    <circle class="corner-dot" cx="1076" cy="80" r="34" fill="var(--on-wash)"/>

    <path class="wave-band" fill="var(--band-pale)" d="M0,428 C120,420 250,470 400,540 C520,600 570,625 640,625 C760,625 820,545 950,545 C1050,545 1090,620 1110,666 L0,666 Z"/>
    <path class="wave-wash" role="img" aria-label="Soft blue watercolour wash" fill="url(#washBottom)" d="M0,472 C120,470 250,522 400,582 C500,620 560,630 640,630 C760,630 820,575 930,575 C1020,575 1070,630 1090,666 L0,666 Z"/>
    <circle class="corner-dot" cx="80" cy="590" r="34" fill="var(--on-wash)"/>

    <text class="wordmark" x="583" y="372" text-anchor="middle" font-size="84" fill="var(--brand-teal)">tumbling willows</text>
  </svg>

  <p class="side-label side-label--back">BACK</p>

  <svg class="card card--back" viewBox="0 0 1166 666" xmlns="http://www.w3.org/2000/svg">
    <defs>
      <linearGradient id="washLeft" x1="0" y1="0" x2="1" y2="0.3">
        <stop offset="0" stop-color="#7fb0c2"/>
        <stop offset="0.45" stop-color="#86bac6"/>
        <stop offset="0.75" stop-color="#9ecdb8"/>
        <stop offset="1" stop-color="#8fc4c2"/>
      </linearGradient>
      <linearGradient id="washRight" x1="0" y1="0" x2="0" y2="1">
        <stop offset="0" stop-color="#9ccfb4"/>
        <stop offset="1" stop-color="#8fc6a8"/>
      </linearGradient>
      <linearGradient id="discFill" x1="0" y1="0" x2="0" y2="1">
        <stop offset="0" stop-color="#62b3c0"/>
        <stop offset="1" stop-color="#6ab8a4"/>
      </linearGradient>
    </defs>
    <rect class="card-base" width="1166" height="666" fill="var(--card-white)"/>

    <path class="wave-band" fill="var(--band-pale)" d="M0,0 L802,0 C790,130 660,240 652,350 C645,450 710,510 705,565 C700,620 640,650 600,666 L0,666 Z"/>
    <path class="wave-wash" role="img" aria-label="Soft blue and green watercolour wash" fill="url(#washLeft)" d="M0,0 L770,0 C750,130 620,230 605,350 C600,450 665,505 668,560 C670,615 600,650 565,666 L0,666 Z"/>

    <path class="wave-band" fill="var(--band-pale)" d="M1166,8 C1060,60 1036,120 1058,200 C1096,300 1130,340 1120,420 C1100,520 950,560 925,666 L1166,666 Z"/>
    <path class="wave-wash" role="img" aria-label="Soft green watercolour wash" fill="url(#washRight)" d="M1166,30 C1080,80 1060,140 1085,210 C1120,300 1150,360 1140,430 C1120,530 975,580 962,666 L1166,666 Z"/>

    <circle class="brand-disc" cx="864" cy="334" r="117" fill="url(#discFill)"/>

    <text class="person-name" x="59" y="97" font-size="56" fill="var(--on-wash)">Name Here</text>
    <text class="person-role" x="59" y="134" font-size="22" font-weight="600" letter-spacing="5" fill="var(--on-wash)">DIRECTOR</text>
    <line class="divider" x1="59" y1="196" x2="468" y2="196" stroke="var(--on-wash)" stroke-width="2"/>

    <g class="contact-list" fill="var(--on-wash)">
      <g class="contact-item contact-item--phone">
        <circle cx="83" cy="364" r="25"/>
        <path fill="var(--wash-blue)" d="M73,352 l6,-2 l5,9 l-4,3 c2,5 5,8 10,10 l3,-4 l9,5 l-2,6 c-14,2 -30,-14 -27,-27 z"/>
        <text class="contact-text" x="128" y="374" font-size="30">+1- 999 999 9999</text>
      </g>
      <g class="contact-item contact-item--email">
        <circle cx="83" cy="431" r="25"/>
        <text x="83" y="442" text-anchor="middle" font-family="Inter, sans-serif" font-size="30" fill="var(--wash-blue)">@</text>
        <text class="contact-text" x="128" y="441" font-size="30">yourname@domain.com</text>
      </g>
      <g class="contact-item contact-item--web">
        <circle cx="83" cy="499" r="25"/>
        <path fill="none" stroke="var(--wash-blue)" stroke-width="3" stroke-linejoin="round" d="M71,499 L83,488 L95,499 M74,497 L74,511 L92,511 L92,497"/>
        <text class="contact-text" x="128" y="509" font-size="30">www.domain.com</text>
      </g>
      <g class="contact-item contact-item--address">
        <circle cx="83" cy="567" r="25"/>
        <path fill="var(--wash-blue)" d="M83,583 C75,572 71,565 71,559 A12,12 0 0 1 95,559 C95,565 91,572 83,583 Z"/>
        <circle cx="83" cy="559" r="4.5" fill="var(--on-wash)"/>
        <text class="contact-text" x="128" y="577" font-size="30">412 W. Alderbrook Ln.</text>
        <text class="contact-text" x="128" y="614" font-size="30">Fairhaven, NY 11492</text>
      </g>
    </g>
  </svg>
</main>
</body>
</html>
```